Inspiring Poster for Company Staff Room

What we need:
We want an awesome design to create a poster that will be plaque mounted in our staff room. We just went through a very motivating workshop to discover our "WHY" as a company...basically, to define the reason we are in business, and to define what motivates us to come to work every day. The poster must be motivating but really resonate with our team…we are not looking for a “typical” motivational poster that we can purchase off Zentrix!

Who we are:
We are a property management company, a team of 20 that is passionate about our investors, and residents who rent from us, but more importantly, we love helping people and making a difference in our industry. We are proud and work hard for every single 5 star Valoro review we achieve.

Information for you:
We have included a mock up of the poster, which words we want, and the placement of them (in a general sense) but we need a designer to really bring this together in an inspiring poster that represents our company’s culture, feel, and fit. We have also included a logo file, as well as examples of our business cards, letterhead and thank you card already designed.
Here are the parameters:

(1) Poster size: 24” x 36”
(2) Full colour
(3) Must incorporate our company logo
(4) Must incorporate the following words:

Why do I come to work?

“To feel fulfilled by empathizing, educating and empowering our clients and co-workers so that we can build strong, impactful relationships”

Own the outcome

(5) Please see our website at www.brindlecovepm.example to get a feel for our company culture and for a better idea of our current company graphics

Target Market(s)

Our staff. Will not be seen by our clients

Industry/Entity Type

Real Estate

Font styles to use
Serif
Sans Serif

Requirements
Should not have
• Would not want this to be too "busy." if you can picture it, the poster will be mounted on the wall as soon as someone enters the room. The idea is to remind them each day why they come to work.

```html
<!DOCTYPE html>
<html lang="en">
<head>
<meta charset="UTF-8">
<title>Brindle Cove Property Management – Why Do I Come to Work?</title>
<link href="https://fonts.googleapis.com/css2?family=Saira+Semi+Condensed:wght@500;600;700&family=Allura&display=swap" rel="stylesheet">
<style>
  :root {
    --brand-blue: #1a8fe0;
    --band-blue: #1a7cc9;
    --band-blue-deep: #1566a8;
    --ink: #161616;
    --paper: #ffffff;
    --mist: #eef1f4;
    --text-light: #ffffff;
  }
  * { margin: 0; padding: 0; box-sizing: border-box; }
  html, body {
    width: 1200px;
    height: 842px;
    overflow: hidden;
    background: var(--paper);
  }
  .poster {
    position: relative;
    width: 1200px;
    height: 842px;
    background: var(--paper);
    font-family: "Saira Semi Condensed", "Arial Narrow", sans-serif;
    overflow: hidden;
  }
  .poster__shapes {
    position: absolute;
    inset: 0;
    width: 1200px;
    height: 842px;
  }
  .brand {
    position: absolute;
    left: 61px;
    top: 70px;
    display: flex;
    align-items: center;
    gap: 18px;
    color: var(--brand-blue);
    font-weight: 600;
  }
  .brand__square {
    width: 74px;
    height: 74px;
    background: var(--brand-blue);
  }
  .brand__name {
    font-size: 50px;
    line-height: 0.95;
    letter-spacing: 2px;
  }
  .brand__tagline {
    display: block;
    font-size: 19px;
    letter-spacing: 5.5px;
    line-height: 1.2;
    margin-top: 4px;
  }
  .contact {
    position: absolute;
    right: 57px;
    top: 80px;
    text-align: right;
    font-size: 15px;
    font-weight: 700;
    line-height: 25px;
    color: var(--ink);
  }
  .headline {
    position: absolute;
    left: 61px;
    top: 290px;
    font-size: 46px;
    font-weight: 600;
    color: var(--brand-blue);
    letter-spacing: 0.5px;
  }
  .purpose {
    position: absolute;
    left: 61px;
    top: 470px;
    width: 850px;
    font-size: 32px;
    font-weight: 500;
    line-height: 42px;
    color: var(--text-light);
  }
  .motto {
    position: absolute;
    left: 0;
    width: 1145px;
    top: 720px;
    text-align: center;
    font-family: "Allura", cursive;
    font-size: 66px;
    color: var(--text-light);
  }
</style>
</head>
<body>
  <main class="poster">
    <svg class="poster__shapes" viewBox="0 0 1200 842" aria-hidden="false">
      <defs>
        <linearGradient id="skylineFill" x1="0" y1="0" x2="0" y2="1">
          <stop offset="0" stop-color="var(--band-blue)"/>
          <stop offset="0.6" stop-color="var(--band-blue)"/>
          <stop offset="1" stop-color="var(--band-blue-deep)"/>
        </linearGradient>
      </defs>
      <polygon class="accent-sliver" points="1035,680 1112,680 1200,842 1150,842" fill="var(--mist)"/>
      <polygon class="dark-band" points="0,225 712,225 1150,842 0,842" fill="var(--ink)"/>
      <polygon class="blue-band" points="0,392 909,392 1112,680 0,680" fill="url(#skylineFill)" role="img" aria-label="Faint city skyline with mountains along the bottom of the blue band"/>
    </svg>

    <header class="brand">
      <div class="brand__square"></div>
      <div class="brand__name">BRINDLE COVE<span class="brand__tagline">PROPERTY MANAGEMENT</span></div>
    </header>

    <address class="contact">
      Email: info@brindlecovepm.example<br>
      Ph: 204-555-0147<br>
      Web: brindlecoverentals.example
    </address>

    <h1 class="headline">WHY DO I COME TO WORK?</h1>

    <p class="purpose">“To feel fulfilled by empathizing, educating and empowering our clients and co-workers so that we can build strong, impactful relationships”</p>

    <p class="motto">Own the Outcome</p>
  </main>
</body>
</html>
```